Business Advisory Firm Business Card

A clean, very upscale looking business card. Not crowded.

Please include logo (attached) and:

Danielle R. Kastrup
Four Ashgrove Court
New York, NY 10087
tel: (917) 555-3140
fax: (646) 555-2973
email: dkastrup@silvermerepartners.example
website: www.silvermerepartners.example

Target Market(s)

Business clients. Often real estate development firms, other advisory firms or growing companies that need assistance. I would like a card that looks impressive and confident.

Industry/Entity Type

Business

Colors

Designer to choose colors to be used in the design.

Requirements
Must have
• Impressive and confident. Please include logo.
Should not have
• nothing flashy...

```html
<!DOCTYPE html>
<html lang="en">
<head>
<meta charset="utf-8">
<title>Silvermere Partners – Business Card</title>
<link rel="stylesheet" href="https://fonts.googleapis.com/css2?family=PT+Sans:wght@400;700&display=swap">
<style>
  :root {
    --page-bg: #e6e6e4;
    --card-white: #ffffff;
    --green: #a4c93c;
    --green-light: #d2e59f;
    --ink: #262626;
    --ink-soft: #3a3a3a;
    --mark-grey: #8d8d8d;
    --rule-grey: #9a9a9a;
    --ghost: rgba(190, 190, 190, 0.32);
  }
  * { box-sizing: border-box; margin: 0; padding: 0; }
  html, body {
    width: 1200px; height: 1000px; overflow: hidden;
    background: var(--page-bg);
    font-family: "PT Sans", Verdana, sans-serif;
  }
  .card {
    position: absolute; left: 100px; top: 214px;
    width: 1000px; height: 571px;
    background: var(--card-white);
    overflow: hidden;
    box-shadow: 0 10px 30px rgba(0,0,0,0.18);
  }
  .card__waves { position: absolute; inset: 0; width: 100%; height: 100%; }
  .brand {
    position: absolute; left: 80px; top: 95px;
    display: flex; align-items: center; gap: 24px;
  }
  .brand__square { width: 110px; height: 110px; background: var(--mark-grey); }
  .brand__rule { width: 2px; height: 150px; background: var(--rule-grey); }
  .brand__name {
    font-size: 38px; font-weight: 400; line-height: 1.05;
    color: var(--ink-soft); text-transform: uppercase; letter-spacing: 1px;
  }
  .contact {
    position: absolute; right: 65px; top: 268px;
    text-align: right; color: var(--ink);
    font-size: 27px; line-height: 38px;
  }
  .contact__name { font-weight: 700; font-size: 30px; }
  .contact__phones { margin-top: 10px; }
  .contact__sep { padding: 0 10px; }
  .contact__web { margin-top: 10px; font-size: 24px; line-height: 32px; }
</style>
</head>
<body>
  <article class="card">
    <svg class="card__waves" viewBox="0 0 1000 571" preserveAspectRatio="none" aria-hidden="true">
      <rect class="ghost-panel" x="770" y="40" width="260" height="290" fill="var(--ghost)"/>
      <path fill="var(--green-light)" d="M0,350 C220,340 380,300 500,250 C610,205 720,195 1000,190 L1000,571 L0,571 Z"/>
      <path fill="none" stroke="var(--card-white)" stroke-width="14" d="M0,412 C220,390 360,345 470,287 C560,240 650,210 1000,202"/>
      <path fill="var(--green)" d="M0,428 C220,405 360,360 470,302 C560,255 650,225 1000,215 L1000,571 L0,571 Z"/>
      <rect x="790" y="60" width="240" height="280" fill="rgba(255,255,255,0.22)"/>
    </svg>

    <header class="brand">
      <div class="brand__square"></div>
      <div class="brand__rule"></div>
      <div class="brand__name">Silvermere<br>Partners,<br>Inc</div>
    </header>

    <section class="contact">
      <p class="contact__name">Danielle R. Kastrup</p>
      <p>Four Ashgrove Court</p>
      <p>New York, NY 10087</p>
      <p class="contact__phones">Tel: (917) 555-3140<span class="contact__sep">|</span>Fax: (646) 555-2973</p>
      <p class="contact__web">E-mail: dkastrup@silvermerepartners.example<br>Website: www.silvermerepartners.example</p>
    </section>
  </article>
</body>
</html>
```